Delmer's Pressure Washing Services

Starting a pressure washing business on my own in Central Valley California, not too much experience so affordable, I do houses, fences, driveways, cars, trailers, RVs. Planning to make this full-time hoping clientele picks up after having a nice business card. Design doesn't have to be flashy, more to the point, I like simplistic/personable. I do not want something exhausting to look at or with too much going on.

Target Market(s)

Residential, Commercial

Industry/Entity Type

Pressure Washing

Contact Information for Business Card

avalible Services

Font styles to use
Sans Serif

Colors
0054AA
0677BA
7BADD7
CADEEF
E8F1F8
0094D4
00A9DD
6FCCEA
C7EBF8
E9F6FB
00AB8E
00BBA5
67D7C9
C6EFE9
E9F9F6

```html
<!DOCTYPE html>
<html lang="en">
<head>
<meta charset="utf-8">
<title>Delmer's Pressure Washing Services – Business Card</title>
<link rel="stylesheet" href="https://fonts.googleapis.com/css2?family=Montserrat:wght@700;800&display=swap">
<style>
  :root {
    --bg: #e9ecf2;
    --navy: #232d86;
    --royal: #2c43a6;
    --white: #ffffff;
    --amber: #c7822c;
    --sky: #1aa8de;
    --sky-soft: #7fd0f0;
    --logo-blue: #2e49b0;
    --mascot-tone: #5a6fb8;
  }
  * { box-sizing: border-box; margin: 0; padding: 0; }
  html, body { width: 1200px; height: 880px; overflow: hidden; }
  body {
    background: var(--bg);
    font-family: "Montserrat", Arial, sans-serif;
    position: relative;
  }
  .card {
    position: absolute;
    left: 250px;
    width: 700px;
    height: 400px;
    border-radius: 22px;
    overflow: hidden;
    box-shadow: 0 10px 28px rgba(20, 30, 70, 0.22);
    background: var(--navy);
  }
  .card--front { top: 26px; }
  .card--back { top: 454px; }
  .card__shapes { position: absolute; inset: 0; width: 100%; height: 100%; }

  .mascot {
    position: absolute;
    border-radius: 40px 40px 18px 18px;
    background: linear-gradient(170deg, var(--mascot-tone), var(--navy));
    opacity: 0.9;
  }
  .card--front .mascot { left: 190px; top: 120px; width: 110px; height: 175px; }
  .card--back .mascot { left: 380px; top: 100px; width: 80px; height: 140px; }

  .brand {
    position: absolute;
    display: flex;
    align-items: center;
    gap: 10px;
    color: var(--logo-blue);
    font-weight: 800;
    text-transform: uppercase;
    line-height: 1.15;
    white-space: nowrap;
  }
  .brand__dot {
    flex: none;
    width: 14px; height: 14px;
    border-radius: 50%;
    background: var(--sky);
  }
  .card--front .brand { left: 325px; top: 158px; font-size: 26px; }
  .card--back .brand { left: 478px; top: 140px; font-size: 15px; gap: 8px; }
  .card--back .brand__dot { width: 12px; height: 12px; }

  .owner {
    position: absolute;
    left: 48px; top: 80px;
    color: var(--white);
    font-weight: 800;
    text-transform: uppercase;
  }
  .owner__name { font-size: 36px; letter-spacing: 0.5px; }
  .owner__phone {
    display: flex; align-items: center; gap: 10px;
    margin-top: 8px;
    font-size: 26px;
    font-weight: 700;
  }
  .owner__phone svg { width: 22px; height: 22px; }

  .services {
    position: absolute;
    left: 48px; top: 246px;
    color: var(--white);
    text-transform: uppercase;
    font-weight: 800;
  }
  .services__title { font-size: 28px; color: var(--sky-soft); margin-bottom: 6px; }
  .services__row { display: flex; align-items: center; gap: 10px; font-size: 20px; line-height: 1.35; }
  .services__sep { width: 9px; height: 9px; border-radius: 50%; background: var(--sky); }
</style>
</head>
<body>

  <section class="card card--front" aria-label="Card front">
    <svg class="card__shapes" viewBox="0 0 700 400" preserveAspectRatio="none" aria-hidden="true">
      <defs>
        <linearGradient id="frontBlue" x1="0" y1="0" x2="1" y2="1">
          <stop offset="0" stop-color="#2e45a8"/>
          <stop offset="1" stop-color="#1f2a80"/>
        </linearGradient>
      </defs>
      <rect width="700" height="400" fill="url(#frontBlue)"/>
      <polygon points="315,0 700,0 700,400 445,400 300,250 290,110" fill="#ffffff"/>
    </svg>
    <div class="mascot" role="img" aria-label="Illustrated worker mascot holding a pressure washer wand"></div>
    <div class="brand">
      <span>Delmer's Pressure<br>Washing Services</span>
      <span class="brand__dot"></span>
    </div>
  </section>

  <section class="card card--back" aria-label="Card back">
    <svg class="card__shapes" viewBox="0 0 700 400" preserveAspectRatio="none" aria-hidden="true">
      <defs>
        <linearGradient id="backBlue" x1="0" y1="0" x2="1" y2="1">
          <stop offset="0" stop-color="#3049ad"/>
          <stop offset="1" stop-color="#1f2a80"/>
        </linearGradient>
      </defs>
      <rect width="700" height="400" fill="url(#backBlue)"/>
      <polygon points="490,0 700,0 700,290 560,215 495,185 455,125" fill="#ffffff"/>
      <path d="M0,0 H380 C330,60 310,150 250,185 C200,215 120,220 0,220 Z" fill="#c7822c"/>
      <path d="M0,375 C140,375 260,355 360,330 C420,318 470,325 520,340 L700,400 H0 Z" fill="#1aa8de"/>
    </svg>
    <div class="owner">
      <div class="owner__name">Delmer Ruiz</div>
      <div class="owner__phone">
        <svg viewBox="0 0 24 24" aria-hidden="true"><path fill="#ffffff" d="M6.6 10.8a15.2 15.2 0 0 0 6.6 6.6l2.2-2.2c.3-.3.7-.4 1-.2 1.1.4 2.3.6 3.6.6.6 0 1 .4 1 1V20c0 .6-.4 1-1 1A17 17 0 0 1 3 4c0-.6.4-1 1-1h3.5c.6 0 1 .4 1 1 0 1.2.2 2.4.6 3.6.1.3 0 .7-.2 1z"/></svg>
        <span>2095 550 148</span>
      </div>
    </div>
    <div class="services">
      <div class="services__title">We Wash</div>
      <div class="services__row"><span>Houses</span><span class="services__sep"></span><span>Fences</span><span class="services__sep"></span><span>Cars</span></div>
      <div class="services__row"><span>Driveways</span><span class="services__sep"></span><span>RVs</span></div>
      <div class="services__row"><span>Trailers</span></div>
    </div>
    <div class="mascot" role="img" aria-label="Illustrated worker mascot holding a pressure washer wand"></div>
    <div class="brand">
      <span>Delmer's Pressure<br>Washing Services</span>
      <span class="brand__dot"></span>
    </div>
  </section>

</body>
</html>
```